Postcard Design for Fertility & Pregnancy Clinic

We are an Australian acupuncture clinic which specialises in treating women who are trying to get pregnant or are already pregnant. The postcard will be attached to our signage outside the building to be taken by prospective clients. We want to convey a professional but welcoming impression. We also want it to look a bit different from the usual pregnancy and fertility type images, e.g. no baby pictures. The signage they are going to be attached to is red so they will probably need to be a different colour to stand out from that which we would probably prefer to be green but are open to other suggestions.

Target Market(s)

Women 25 - 45 years

Industry/Entity Type

Alternative Medicine

Requirements
Must have
• Vertical design, front and back of the postcard with the text on the back of the card
Nice to have
• I like illustrations more than photos.
Should not have
• Generic baby or pregnancy photos

```html
<!DOCTYPE html>
<html lang="en">
<head>
<meta charset="utf-8">
<title>Willow Bloom Acupuncture Clinic – Postcard</title>
<link href="https://fonts.googleapis.com/css2?family=Barlow:wght@400;600;700&family=Barlow+Semi+Condensed:wght@300;400;500&display=swap" rel="stylesheet">
<style>
  :root {
    --page-bg: #ecebe6;
    --card-white: #ffffff;
    --text-grey: #545454;
    --panel-green: #e6eccb;
    --frame-green: #d3e27a;
    --rule-green: #dfe6b8;
    --brand-red: #e8372a;
    --brand-text: #ffffff;
    --photo-dark: #3f5a3a;
    --photo-mid: #8fa462;
    --photo-light: #d8d9a4;
  }
  * { box-sizing: border-box; margin: 0; padding: 0; }
  html, body { width: 1200px; height: 1000px; overflow: hidden; }
  body {
    background: var(--page-bg);
    position: relative;
    font-family: "Barlow", Arial, sans-serif;
    color: var(--text-grey);
  }

  /* ---------- Shared brand tile ---------- */
  .brand-tile {
    position: absolute; background: var(--brand-red);
    display: flex; flex-direction: column; align-items: center; justify-content: center;
    color: var(--brand-text); font-family: "Barlow Semi Condensed", Arial, sans-serif;
    font-weight: 400; text-align: center;
  }
  .brand-tile .mark { border-radius: 50%; background: var(--brand-text); }

  /* ---------- Back of card (portrait) ---------- */
  .card-back {
    position: absolute; left: 60px; top: 140px;
    width: 520px; height: 720px;
    background: var(--card-white);
    box-shadow: 0 2px 6px rgba(0,0,0,.18);
  }
  .card-back .brand-tile {
    left: 20px; top: 20px; width: 180px; height: 124px;
    font-size: 16px; line-height: 17px; gap: 12px;
  }
  .card-back .brand-tile .mark { width: 34px; height: 34px; }
  .stamp-box {
    position: absolute; right: 20px; top: 20px; width: 110px; height: 130px;
    border: 1px solid var(--rule-green);
  }
  .intro {
    position: absolute; left: 20px; top: 166px; width: 480px;
    font-size: 15px; line-height: 20px;
  }
  .intro strong { font-weight: 700; }
  .info-panel {
    position: absolute; left: 16px; top: 254px;
    width: 488px; height: 442px;
    background: var(--panel-green);
    padding: 14px 16px;
    font-size: 14px; line-height: 18px;
  }
  .info-panel strong { font-weight: 700; }
  .conditions-title { font-weight: 700; margin-top: 14px; font-size: 14px; }
  .conditions {
    display: grid; grid-template-columns: 210px 1fr;
    font-size: 12px; line-height: 14.5px; margin-top: 5px;
  }
  .conditions ul { list-style: none; }
  .cta { font-weight: 700; margin-top: 16px; font-size: 13.5px; line-height: 17px; }
  .contact { margin-top: 12px; font-size: 13px; line-height: 16px; }
  .address { margin-top: 10px; font-size: 13px; line-height: 16px; }

  /* ---------- Front of card (portrait) ---------- */
  .card-front {
    position: absolute; left: 620px; top: 140px;
    width: 520px; height: 720px;
    background: var(--frame-green);
    box-shadow: 0 3px 8px rgba(0,0,0,.22);
  }
  .hero-photo {
    position: absolute; left: 20px; top: 20px; width: 480px; height: 680px;
    background:
      radial-gradient(ellipse at 85% 8%, #f3f1d6 0%, transparent 45%),
      linear-gradient(100deg, var(--photo-dark) 0%, #5f7a4c 30%, var(--photo-mid) 58%, var(--photo-light) 100%);
  }
  .hero-photo::after {
    content: ""; position: absolute; left: 0; right: 0; bottom: 0; height: 38%;
    background: linear-gradient(180deg, transparent, rgba(196,180,90,.55));
  }
  .headline-band {
    position: absolute; left: 20px; top: 290px; width: 300px; height: 132px;
    background: rgba(255,255,255,.16);
    font-family: "Barlow Semi Condensed", Arial, sans-serif; font-weight: 300;
    color: #ffffff; text-align: center; padding: 10px 12px 0 0;
  }
  .headline-band::after {
    content: ""; position: absolute; right: 0; top: 0; width: 9px; height: 100%; background: #ffffff;
  }
  .headline-band p { font-size: 19px; line-height: 24px; }
  .headline-band .big { font-size: 28px; line-height: 32px; font-weight: 400; }
  .headline-band .mid { font-size: 21px; line-height: 28px; }
  .headline-band .mid b { font-weight: 400; }
  .card-front .brand-tile {
    left: 70px; top: 570px; width: 140px; height: 100px;
    font-size: 13.5px; line-height: 14px; gap: 9px;
  }
  .card-front .brand-tile .mark { width: 26px; height: 26px; }
</style>
</head>
<body>

<section class="card-back" aria-label="Postcard back">
  <div class="brand-tile">
    <span class="mark"></span>
    <span>Willow Bloom<br>Acupuncture Clinic</span>
  </div>
  <div class="stamp-box"></div>

  <p class="intro">Here at <strong>The Willow Bloom Acupuncture Clinic</strong> we focus on those wanting to conceive or who are already pregnant and whatever your concerns are, we'd love to help you.</p>

  <div class="info-panel">
    <p><strong>Acupuncture</strong> is an effective and safe method of improving your general health in order to increase your chances of conceiving and/or of having the pregnancy you desire. We combine our acupuncture techniques with lots of lifestyle and nutritional advice tailored just for you.</p>
    <p class="conditions-title">Common conditions we see at the clinic include:</p>
    <div class="conditions">
      <ul>
        <li>PCOS</li><li>Endometriosis</li><li>Irregular or no periods</li><li>Poor ovarian reserve</li>
        <li>Recurrent implantation failure</li><li>IVF Support</li><li>Embryo transfer treatments</li>
      </ul>
      <ul>
        <li>Stress and anxiety</li><li>Morning sickness</li><li>Breech babies</li><li>Hip and back pain in pregnancy</li>
        <li>Carpal tunnel</li><li>Pre-birth acupuncture</li><li>Natural induction of labour</li>
      </ul>
    </div>
    <p class="cta">Please check out the website for further information or give us a call if you'd like an appointment.</p>
    <p class="contact">Phone: 07 3555 0142<br>hello@willowbloomacupuncture.com.au<br>www.willowbloomacupuncture.com.au</p>
    <p class="address">Level 4, Banksia Health Centre,<br>118 Ferndale Tce, Hillview,<br>Qld, 4000.</p>
  </div>
</section>

<section class="card-front" aria-label="Postcard front">
  <div class="hero-photo" role="img" aria-label="Photo of a woman sitting in a sunlit grassy meadow with hills behind and leaves in the foreground"></div>
  <div class="headline-band">
    <p>Are you</p>
    <p class="big">trying to have a baby</p>
    <p class="mid">or <b>experiencing a difficulty</b></p>
    <p>in your current pregnancy?</p>
  </div>
  <div class="brand-tile">
    <span class="mark"></span>
    <span>Willow Bloom<br>Acupuncture Clinic</span>
  </div>
</section>

</body>
</html>
```